Yoga and Wellness Center

New business- have the logo already, but wanted my cards to be more colorful.

Please find my attached logo. I am only waiting on confirmation of my
telephone number in order to have all the information right. This is for a
new yoga and wellness center in TN for a conservative audience, but I would
like a colorful business card.

Industry/Entity Type

Conservative

```html
<!DOCTYPE html>
<html lang="en">
<head>
<meta charset="utf-8">
<title>Cedar Hollow Yoga – Business Card</title>
<link href="https://fonts.googleapis.com/css2?family=Lato:wght@400;700;900&display=swap" rel="stylesheet">
<style>
  :root {
    --backdrop: #2f2f31;
    --card-white: #ffffff;
    --card-shade: #ececec;
    --navy: #24307a;
    --orange-light: #e0602a;
    --orange-deep: #b9441a;
    --text-light: #ffffff;
    --name-tint: #f0ddd2;
  }
  * { margin: 0; padding: 0; box-sizing: border-box; }
  html, body {
    width: 1200px;
    height: 1116px;
    overflow: hidden;
    background: var(--backdrop);
    font-family: "Lato", Arial, sans-serif;
  }
  .business-card {
    position: absolute;
    left: 100px;
    top: 272px;
    width: 1000px;
    height: 572px;
    background: linear-gradient(180deg, var(--card-white) 0%, var(--card-shade) 100%);
    box-shadow: 0 18px 40px rgba(0,0,0,0.55);
    overflow: hidden;
  }
  .card-waves {
    position: absolute;
    inset: 0;
    width: 100%;
    height: 100%;
  }
  .brand {
    position: absolute;
    left: 400px;
    top: 110px;
    transform: translateX(-50%);
    display: flex;
    align-items: center;
    gap: 16px;
    white-space: nowrap;
  }
  .brand-dot {
    width: 40px;
    height: 40px;
    border-radius: 50%;
    background: var(--orange-light);
  }
  .brand-name {
    font-weight: 900;
    font-size: 34px;
    letter-spacing: 5px;
    color: var(--navy);
  }
  .owner {
    position: absolute;
    right: 70px;
    top: 225px;
    text-align: center;
  }
  .owner-name {
    font-weight: 900;
    font-size: 34px;
    color: var(--name-tint);
  }
  .owner-title {
    margin-top: 4px;
    font-weight: 400;
    font-size: 18px;
    letter-spacing: 1px;
    color: var(--name-tint);
  }
  .contact-list {
    position: absolute;
    left: 56px;
    top: 360px;
    list-style: none;
    color: var(--text-light);
    font-size: 26px;
    line-height: 1.25;
  }
  .contact-item {
    display: flex;
    align-items: flex-start;
    gap: 16px;
    margin-bottom: 14px;
  }
  .contact-icon {
    width: 24px;
    height: 24px;
    flex: 0 0 24px;
    margin-top: 5px;
    fill: var(--text-light);
  }
</style>
</head>
<body>
  <div class="business-card">
    <svg class="card-waves" viewBox="0 0 1000 572" preserveAspectRatio="none" aria-hidden="true">
      <defs>
        <linearGradient id="orangeField" x1="0" y1="0" x2="1" y2="1">
          <stop offset="0" stop-color="#e0602a"/>
          <stop offset="1" stop-color="#b9441a"/>
        </linearGradient>
      </defs>
      <path d="M0,300 C320,250 680,160 1000,132 L1000,572 L0,572 Z" fill="#24307a"/>
      <path d="M0,314 C320,266 680,180 1000,154 L1000,572 L0,572 Z" fill="url(#orangeField)"/>
    </svg>

    <div class="brand">
      <span class="brand-dot"></span>
      <span class="brand-name">CEDAR HOLLOW YOGA</span>
    </div>

    <div class="owner">
      <p class="owner-name">Daniel Hartley</p>
      <p class="owner-title">OWNER / FOUNDER</p>
    </div>

    <ul class="contact-list">
      <li class="contact-item">
        <svg class="contact-icon" viewBox="0 0 24 24" aria-hidden="true"><path d="M6.6 10.8a15.1 15.1 0 0 0 6.6 6.6l2.2-2.2a1 1 0 0 1 1-.25 11.4 11.4 0 0 0 3.6.57 1 1 0 0 1 1 1V20a1 1 0 0 1-1 1A17 17 0 0 1 3 4a1 1 0 0 1 1-1h3.5a1 1 0 0 1 1 1c0 1.25.2 2.45.57 3.57a1 1 0 0 1-.25 1z"/></svg>
        <span>(555) 014-2298</span>
      </li>
      <li class="contact-item">
        <svg class="contact-icon" viewBox="0 0 24 24" aria-hidden="true"><path d="M2 5h20v14H2z M2 5l10 8 10-8" fill="none" stroke="#fff" stroke-width="2"/></svg>
        <span>daniel@cedarhollow.com</span>
      </li>
      <li class="contact-item">
        <svg class="contact-icon" viewBox="0 0 24 24" aria-hidden="true"><path d="M12 2a7 7 0 0 0-7 7c0 5 7 13 7 13s7-8 7-13a7 7 0 0 0-7-7zm0 9.5A2.5 2.5 0 1 1 12 6.5a2.5 2.5 0 0 1 0 5z"/></svg>
        <span>2150 Maple Grove Rd., Ste. 110<br>Franklin, Tennessee 37064</span>
      </li>
    </ul>
  </div>
</body>
</html>
```